Tidewell show guide

I need to design a one page 7x10 pdf that will be printed. It will include our logo and the following text:

#1 Disaster Mitigation Lead Platform

We generated over 60 million in
revenue last year fo our contractors.

Leads types:
-Water Damage
-Fire Damage
-Mold Remediation
-Biohazard
-Plumbing
-Carpet Cleaning

Exclusive leads
No monthly fees
Only pay for valid leads

Stop by booth 814 to get to your cut!

Target Market(s)

Home service contractors

Colors
9bcb3b
0255a3

Requirements
Must have
• our logo and text
Should not have
• any clutter

```html
<!DOCTYPE html>
<html lang="en">
<head>
<meta charset="utf-8">
<title>Crestline Leads – Show Guide</title>
<link rel="stylesheet" href="https://fonts.googleapis.com/css2?family=Open+Sans:wdth,wght@75..100,400..800&display=swap">
<style>
  :root {
    --brand-blue: #0255a3;
    --brand-green: #9bcb3b;
    --ink-dark: #1f1f1f;
    --ink-text: #1d1d1d;
    --paper: #ffffff;
    --faint-blue: #dde6f1;
  }
  * { margin: 0; padding: 0; box-sizing: border-box; }
  html, body {
    width: 800px; height: 1200px; overflow: hidden;
    background: var(--paper);
    font-family: "Open Sans", Arial, sans-serif;
  }
  .page { position: relative; width: 800px; height: 1200px; overflow: hidden; }
  .backdrop { position: absolute; inset: 0; }

  .brand {
    position: absolute; top: 66px; left: 0; width: 800px;
    display: flex; align-items: center; justify-content: center; gap: 24px;
  }
  .brand-mark {
    width: 112px; height: 112px; border-radius: 50%;
    border: 9px solid var(--brand-green);
  }
  .brand-name {
    color: var(--brand-green); font-weight: 600; font-size: 46px;
    letter-spacing: 6px; text-transform: uppercase;
  }

  .headline { position: absolute; left: 0; top: 312px; width: 800px; color: var(--paper); font-weight: 800; font-stretch: 85%; }
  .headline-rank {
    position: absolute; left: 92px; top: 0;
    font-size: 168px; line-height: 150px; letter-spacing: -4px;
  }
  .headline-topic {
    position: absolute; left: 300px; top: 12px;
    font-size: 80px; line-height: 66px; letter-spacing: -0.5px;
  }
  .headline-sub {
    position: absolute; left: 0; top: 148px; width: 800px; text-align: center;
    color: var(--brand-green); font-size: 92px; line-height: 92px; letter-spacing: 0.5px;
  }

  .claim {
    position: absolute; left: 0; top: 566px; width: 800px; text-align: center;
    color: var(--paper); font-size: 32px; line-height: 45px; font-weight: 400;
  }
  .claim strong { color: var(--brand-green); font-weight: 700; }

  .booth {
    position: absolute; left: 0; top: 662px; width: 800px; text-align: center;
    color: var(--paper); font-size: 25px; line-height: 32px; font-weight: 700;
  }
  .booth strong { color: var(--brand-green); }

  .benefits {
    position: absolute; left: 72px; top: 872px; list-style: none;
    font-size: 32px; font-weight: 600; color: var(--ink-text); line-height: 46px;
  }
  .benefits li { display: flex; gap: 10px; margin-bottom: 4px; }
  .benefits .tick { color: var(--brand-blue); font-weight: 400; width: 24px; }

  .lead-types {
    position: absolute; left: 455px; top: 790px; color: var(--paper);
  }
  .lead-types h2 { font-size: 33px; font-weight: 700; letter-spacing: 0.5px; }
  .lead-types .rule { width: 48px; height: 5px; background: var(--brand-blue); margin: 6px 0 18px; }
  .lead-types ul { list-style: none; font-size: 26px; line-height: 39px; font-weight: 400; }
  .lead-types li::before { content: "✓"; color: rgba(255,255,255,0.7); margin-right: 10px; font-size: 20px; }

  .footer {
    position: absolute; left: 0; top: 1127px; width: 800px; height: 73px;
    background: var(--brand-blue); color: var(--paper);
    display: flex; align-items: center; justify-content: center; gap: 54px;
    font-size: 31px; font-weight: 700;
  }
  .footer-item { display: flex; align-items: center; gap: 10px; }
</style>
</head>
<body>
<div class="page">
  <svg class="backdrop" width="800" height="1200" viewBox="0 0 800 1200" aria-hidden="true">
    <polygon points="0,240 705,186 705,192 0,282" fill="var(--brand-green)"/>
    <polygon points="0,287 800,172 800,702 0,806" fill="var(--brand-blue)"/>
    <polygon points="0,806 800,686 800,716 0,812" fill="var(--ink-dark)"/>
    <circle cx="250" cy="1010" r="190" fill="none" stroke="var(--faint-blue)" stroke-width="34" opacity="0.6"/>
    <polygon points="409,752 752,707 752,1127 409,1127" fill="var(--brand-green)"/>
  </svg>

  <header class="brand">
    <span class="brand-mark"></span>
    <span class="brand-name">Crestline Leads</span>
  </header>

  <h1 class="headline">
    <span class="headline-rank">#1</span>
    <span class="headline-topic">DISASTER<br>MITIGATION</span>
    <span class="headline-sub">LEAD PLATFORM</span>
  </h1>

  <p class="claim">We generated <strong>over 60 million</strong> in<br>revenue last year for our contractors.</p>
  <p class="booth">Stop by <strong>booth 814</strong> to get your cut!</p>

  <ul class="benefits">
    <li><span class="tick">✓</span><span>Exclusive leads</span></li>
    <li><span class="tick">✓</span><span>No monthly fees</span></li>
    <li><span class="tick">✓</span><span>Only pay<br>for valid leads</span></li>
  </ul>

  <section class="lead-types">
    <h2>LEADS TYPES:</h2>
    <div class="rule"></div>
    <ul>
      <li>Water Damage</li>
      <li>Fire Damage</li>
      <li>Mold Remediation</li>
      <li>Biohazard</li>
      <li>Plumbing</li>
      <li>Carpet Cleaning</li>
    </ul>
  </section>

  <footer class="footer">
    <span class="footer-item">
      <svg width="30" height="30" viewBox="0 0 30 30" aria-hidden="true" fill="none" stroke="#fff" stroke-width="2.4">
        <circle cx="15" cy="15" r="12"/><ellipse cx="15" cy="15" rx="5.5" ry="12"/><line x1="3" y1="15" x2="27" y2="15"/><line x1="5" y1="9" x2="25" y2="9"/><line x1="5" y1="21" x2="25" y2="21"/>
      </svg>
      crestlineleads.com
    </span>
    <span class="footer-item">
      <svg width="30" height="30" viewBox="0 0 30 30" aria-hidden="true" fill="none" stroke="#fff" stroke-width="2.4">
        <circle cx="15" cy="15" r="12.5"/>
        <path d="M10.5 8.5l3 3-1.8 2a9 9 0 0 0 4.8 4.8l2-1.8 3 3-2 2.2c-5 0-11.2-6.2-11.2-11.2z" fill="#fff" stroke="none"/>
      </svg>
      1-888-555-0142
    </span>
  </footer>
</div>
</body>
</html>
```